Pellano Growth Brochure Design Project

- Who we are?
Pellano Growth is New Internet Marketing Company Based in China.

It is our aim to provide Chinese clients with the means to internationally market their product, via the Internet.

Our primary products are Outsourced Design ( Thanks to Artwell hub and the amazing designers who use it), SEO and Virtual Hosting.

- Project Brief
Design a vibrant and fresh brochure that introduces the fundamentals of SEO. There is no restriction to the number of pages, however all the info I have included in this brief must be included.

- Colour Palette
Please see link or download the Vantoria Swatch Exchange File or follow the link below
http://hues.vantoria-sample.com/#themes/search?term=4817350

Logo updated - grey background removed

Various file formats added for logo and brochure content

Brochure zip file add containing logo in different formats.

Vantoria color scheme file added

The general corporate colors are:

Base Color: CMYK :0, 60, 80, 0  Hex: FF6633
Dark Orange: CMYK: 0, 72, 96, 30 Hex: B23308
Light Orange: CMYK 0, 42, 56, 0 Hex: FF9571
Grey: CMYK 0, 0, 0, 48 Hex: 858585
Light Grey: CMYK 0, 0, 0, 26 Hex: BDBDBD

Please note that I'm happy for other colors to be included, however I would like these the corporate branding colors to be clearly present through the brochure.

Hi All

First place payment has increased to $600 - Looking to see some creative designs!

Hi All

Reason: I have increase the budget and extend the deadline as I need to see more design.

I have attached a zip file that contains example brochures I like.

We are not keen on the table data its a little plain. We have create an info-graphic to replace one of the table and would like to see it included in the design.

Reason: A few designers have asked for this extension and I would like to see additional designs. Thanks Marek

Target Market(s)

- Our Target Audience is..
It is small to medium businesses looking to reach out to the international market.
Our clients still very much operate on a face to face level in business and are new to the concept of Internet marketing

However this must look professional, Marketable and Clean, with the power of connecting people globally, through SEO and design to be reflected visually in the brochure.

Industry/Entity Type

Internet

Requirements
Must have
• One or more of the FACTS that I have highlighted need to stand out on each page. These FACTS can be found the document attached to this brief and are under the section titled 'Did You Know!'. Not every fact in this section needs to be highlighted in the brochure, but each page needs to have at least, one or more fact that stands out, soemwhere on the page.
See attached document, under the heading 'Did you Know!' and use one or two of these facts to spruce up the pages!

One image/ per page or per two pages MUST be included!

- Provide stock photos and please send us a message with the additional cost of these with your submission

The Table data, that I have included in the attachment must be included in the body of the pages - BUT the table format is not necessary and you can place the information in the body like plain text.

The brochure size should be a little larger than A4.

Please design the back page, like a pocket to hold paper and other material in it that I include with this brochure.

```html
<!DOCTYPE html>
<html lang="en">
<head>
<meta charset="utf-8">
<title>Pellano Growth Brochure – Spreads 8 to 11</title>
<link rel="stylesheet" href="https://fonts.googleapis.com/css2?family=Raleway:wght@200;300&family=Open+Sans:wght@400;600;700&display=swap">
<style>
:root{
  --base-orange:#ff6633;
  --dark-orange:#b23308;
  --light-orange:#ff9571;
  --label-orange:#f0957a;
  --grey:#858585;
  --light-grey:#bdbdbd;
  --slate:#8a9ca6;
  --slate-dark:#5f727c;
  --table-head:#a9b3b8;
  --table-cell:#dfe4e6;
  --ink:#444;
  --paper:#ffffff;
  --backdrop:#e4e4e4;
}
*{box-sizing:border-box;margin:0;padding:0}
html,body{width:1200px;height:900px;overflow:hidden;background:var(--backdrop)}
body{font-family:"Open Sans",Arial,sans-serif;color:var(--ink)}
.canvas{position:relative;width:1200px;height:900px}
.spread{position:absolute;background:var(--paper);overflow:hidden}
.fold{position:absolute;top:0;bottom:0;border-left:1px dashed #c9c9c9}
.page-number{position:absolute;font-size:15px;color:#222}
.rule{position:absolute;height:1px;background:var(--light-orange)}
.rule--slate{background:var(--slate-dark)}
.site-url{position:absolute;font-size:4px;letter-spacing:.4px;color:var(--light-grey)}
.section-title{position:absolute;font-family:"Raleway",Arial,sans-serif;font-weight:200;font-size:21px;letter-spacing:0;color:#555;line-height:1;white-space:nowrap}
.label{position:absolute;height:11px;background:var(--label-orange);color:#fff;font-size:5px;line-height:11px;padding:0 4px;letter-spacing:.2px;white-space:nowrap}
.body-copy{position:absolute;font-size:4px;line-height:1.35;color:#555}
.body-copy p+p{margin-top:3px}
.body-copy strong{font-weight:700;color:#333;font-size:4.6px}
.drop-cap{float:left;font-family:"Raleway",Arial,sans-serif;font-size:22px;line-height:18px;margin:0 3px 0 0;color:var(--light-orange)}
.drop-cap--grey{color:var(--grey)}
.page-tab{position:absolute;width:9px;height:9px;background:var(--base-orange);color:#fff;font-size:4px;line-height:9px;text-align:center}
.photo{position:absolute}

/* spread 8 */
.spread--cover{left:35px;top:60px;width:540px;height:375px}
.cover-photo{left:0;top:0;width:540px;height:375px;background:linear-gradient(100deg,#2d3c56 0%,#4c5d79 35%,#8b8a92 62%,#6b5a55 80%,#3d3a42 100%)}
.cover-quote{position:absolute;left:20px;top:268px;border-left:2px solid #fff;padding-left:6px;color:#fff;font-weight:600;font-size:11.5px;line-height:13px;width:98px}

/* spread 9 */
.spread--design{left:625px;top:60px;width:540px;height:372px}
.design-art{position:absolute;left:0;top:30px}
.design-process{position:absolute;left:180px;top:228px;width:88px;height:117px;background:var(--table-cell);padding:5px 4px;font-size:4px;line-height:1.35;color:#555}
.design-process p+p{margin-top:3px}
.design-process b{color:var(--dark-orange)}
.compare-table{position:absolute;left:288px;top:93px;width:232px;border-collapse:collapse;table-layout:fixed;font-size:3.6px;line-height:1.1;color:#555}
.compare-table th,.compare-table td{border:1px solid #fff;padding:1px 2px;vertical-align:middle;text-align:left}
.compare-table thead th{background:var(--table-head);color:#fff;font-weight:400;text-align:center;font-size:5px;height:11px}
.compare-table thead th.empty{background:none}
.compare-table tbody th{background:var(--table-head);color:#fff;font-weight:400}
.compare-table tbody td{background:var(--table-cell)}
.stat{position:absolute;left:372px;top:228px;border-left:2px solid var(--light-orange);padding-left:4px;width:150px;font-size:11.5px;line-height:12px;font-weight:600;color:var(--grey)}
.stat-line{display:block;white-space:nowrap}
.stat-line--figure{height:26px;line-height:26px}
.stat-figure{color:var(--light-orange);font-size:26px;font-weight:700;letter-spacing:-.5px}

/* spread 10 */
.spread--cases{left:35px;top:465px;width:540px;height:380px}
.screenshot{background:linear-gradient(180deg,#c21d2e 0%,#9a1424 22%,#e8e8e8 23%,#8c8c8c 60%,#e6e6e6 100%);border:1px solid #bbb}
.thumb-purple{background:linear-gradient(180deg,#5b1a6e,#b736b8 50%,#8e2b9c)}
.thumb-dark{background:linear-gradient(180deg,#1a1a1a,#3a2f3a 50%,#111)}
.thumb-violet{background:linear-gradient(180deg,#eaeaea 0%,#c340c4 25%,#a224b0 100%)}
.caption{position:absolute;font-size:4.5px;color:#333}
.logo-panel{position:absolute;background:#fff;border:1px solid #cfcfcf;display:flex;align-items:center;justify-content:center;font-family:"Open Sans",Arial,sans-serif;font-weight:700;color:#2f5aa8;white-space:nowrap}
.logo-panel--large{left:292px;top:175px;width:154px;height:172px;font-size:19px}
.logo-panel--small{left:455px;width:74px;height:52px;font-size:8px}

/* spread 11 */
.spread--pocket{left:625px;top:467px;width:540px;height:375px}
.pocket-panel{position:absolute;left:270px;top:0}
</style>
</head>
<body>
<main class="canvas">

  <!-- Spread 8: cloud hosting opener -->
  <section class="spread spread--cover" aria-label="Spread 8">
    <div class="photo cover-photo" role="img" aria-label="Stock photo: a woman sketching a cloud computing diagram with network, laptop, mobile and database icons on a glass board"></div>
    <div class="fold" style="left:272px;border-color:rgba(255,255,255,.25)"></div>
    <p class="cover-quote">The Location of you website/ server makes a difference to who gets to see it</p>
  </section>
  <span class="page-number" style="left:563px;top:442px">8</span>

  <!-- Spread 9: website design -->
  <section class="spread spread--design" aria-label="Spread 9">
    <div class="rule" style="left:20px;top:23px;width:230px"></div>
    <div class="rule" style="left:287px;top:23px;width:233px"></div>
    <span class="site-url" style="left:458px;top:17px">WWW.PELLANOGROWTH.COM</span>
    <div class="fold" style="left:268px"></div>

    <svg class="design-art" width="180" height="342" viewBox="0 0 180 342" aria-hidden="true">
      <defs>
        <clipPath id="design-photo-clip"><circle cx="15" cy="200" r="148"/></clipPath>
        <linearGradient id="design-photo-tone" x1="0" y1="0" x2="1" y2="1">
          <stop offset="0" stop-color="#d9d4cf"/>
          <stop offset=".5" stop-color="#9a8f88"/>
          <stop offset="1" stop-color="#3a3c44"/>
        </linearGradient>
      </defs>
      <circle cx="15" cy="200" r="172" fill="none" stroke="#c7cdd0" stroke-width="6"/>
      <circle cx="15" cy="200" r="160" fill="none" stroke="#8e9aa0" stroke-width="10"/>
      <rect x="-140" y="52" width="320" height="300" fill="url(#design-photo-tone)" clip-path="url(#design-photo-clip)" role="img" aria-label="Stock photo: a designer's hand working with a stylus on a graphics tablet"/>
    </svg>

    <h2 class="section-title" style="left:82px;top:46px">WEBSITE DESIGN</h2>
    <span class="label" style="left:145px;top:71px">WHY CHOOSE PELLANO GROWTH?</span>

    <div class="body-copy" style="left:180px;top:90px;width:78px">
      <p><span class="drop-cap">A</span>professional design is key to making sure that your visitors feel comfortable purchasing from you. Our designers have been designing sites that people trust for years.</p>
      <p><strong>Why choose Pellano Growth?</strong></p>
      <p>Here at Pellano Growth we believe that competition is great! Competition is what drives us to be better so we have applied this to our design process. We also believe that you should only pay for the designs you like! Designers only enter competitions in their area of expertise, this means you only get the best people working on your project and, best of all, you only pay for your favourites.</p>
    </div>

    <span class="label" style="left:180px;top:217px;width:88px">THE DESIGN PROCESS</span>
    <div class="design-process">
      <p><b>7.</b> Together we will create a unique design brief that meets your requirements</p>
      <p><b>8.</b> Pellano Growth will post the competition and invite 100's to 1000's of international designers to take part</p>
      <p><b>9.</b> Our designers will submit their high quality designs.</p>
      <p><b>10.</b> Using our online portal you can supply feedback and suggest any changes you would like, then we pass these on to our designers.</p>
      <p><b>11.</b> The designers update their designs.</p>
      <p><b>12.</b> You pick the winners and those designers get paid!</p>
    </div>

    <span class="label" style="left:288px;top:71px">ONLINE MARKETING AND SEO VS TRADITIONAL</span>
    <table class="compare-table">
      <colgroup><col style="width:35px"><col style="width:30px"><col style="width:62px"><col style="width:30px"><col style="width:75px"></colgroup>
      <thead>
        <tr><th class="empty"></th><th colspan="2">OUR METHOD</th><th colspan="2">TRADITIONAL</th></tr>
      </thead>
      <tbody>
        <tr style="height:19px"><th>Cost</th><td>Low Cost</td><td>You only pay for the winning designs - you don't pay for anything else</td><td>High Cost</td><td>Traditional design companies have to cover the cost of the designers on every project, you ultimately pay for these costs</td></tr>
        <tr style="height:11px"><th>Number of Designs</th><td>A lot</td><td>20 - 100+</td><td>A few</td><td>3-7</td></tr>
        <tr style="height:25px"><th>Variety of Designs</th><td>Many unique International Designs</td><td>Many of your designs will come from different people from all over the globe, this ensures that every design is unique</td><td>A few similar designs</td><td>Many design companies have all its designers in a single location, and only assign 1 or 2 designers to your project, so the design progress becomes stale.</td></tr>
        <tr style="height:15px"><th>Number of designers</th><td>Many International Designers</td><td>15-60+</td><td>A small departmental team</td><td>2-3</td></tr>
        <tr style="height:12px"><th>Number of changes</th><td></td><td>Too many to count</td><td></td><td>2-3 on a single design</td></tr>
        <tr style="height:18px"><th>Number of designers to choose from</th><td>100000+</td><td>We have thousands of freelance designers who we invite to your project</td><td>5-10000</td><td>Even the biggest design companies can only spare a few employees to work on a project.</td></tr>
      </tbody>
    </table>
    <span class="page-tab" style="left:527px;top:183px">15</span>

    <span class="label" style="left:288px;top:233px">HOW LONG DOES</span>
    <span class="label" style="left:288px;top:246px">IT TAKE?</span>
    <div class="body-copy" style="left:288px;top:262px;width:78px">
      <p>Normally a design project takes between 10 and 15 days - but don't worry if you are in a rush! We have created projects with amazing results in less than 5 days.</p>
    </div>

    <p class="stat">
      <span class="stat-line stat-line--figure"><span class="stat-figure">40%</span> of SEO</span>
      <span class="stat-line">campaigns aware of their</span>
      <span class="stat-line">ROI achieve returns in</span>
      <span class="stat-line stat-line--figure">excess of <span class="stat-figure">500%</span></span>
    </p>
  </section>
  <span class="page-number" style="left:1153px;top:439px">9</span>

  <!-- Spread 10: case studies -->
  <section class="spread spread--cases" aria-label="Spread 10">
    <div class="rule" style="left:20px;top:25px;width:235px"></div>
    <div class="rule" style="left:292px;top:25px;width:236px"></div>
    <span class="site-url" style="left:466px;top:20px">WWW.PELLANOGROWTH.COM</span>
    <div class="fold" style="left:272px"></div>

    <h2 class="section-title" style="left:20px;top:50px">CASE STUDIES</h2>
    <span class="label" style="left:20px;top:75px">SITE DESIGNS: VERALIN.COM</span>
    <div class="body-copy" style="left:20px;top:94px;width:75px">
      <p><span class="drop-cap drop-cap--grey">L</span>Veralin is Asia's leading provider in market expansion services for the health and wellness industry. Based in Europe, we operate from locations in Hong Kong and China and serve markets all over Asia. They are the Head Representative Agent in Asia for</p>
    </div>
    <div class="body-copy" style="left:100px;top:94px;width:76px">
      <p>many leading international brands of quality wellness consumer products. They had received feedback for business partners that their website was not very professional.</p>
      <p>Veralin received over 30 different designs in less than 10 days.</p>
    </div>
    <span class="label" style="left:20px;top:155px">VERALIN WINNER CHOICE</span>
    <div class="photo screenshot" role="img" aria-label="Winning website design for Veralin: red header with product banner and grey content area" style="left:20px;top:168px;width:153px;height:179px"></div>
    <div class="photo thumb-purple" role="img" aria-label="Alternative website design in purple" style="left:182px;top:75px;width:73px;height:92px"></div>
    <div class="photo thumb-dark" role="img" aria-label="Alternative website design in black" style="left:182px;top:172px;width:73px;height:91px"></div>
    <div class="photo thumb-violet" role="img" aria-label="Alternative website design in violet" style="left:182px;top:268px;width:73px;height:79px"></div>
    <p class="caption" style="left:20px;top:348px">A selection of the 30 different designs that Veralin received</p>
    <div class="rule" style="left:20px;top:355px;width:235px"></div>

    <span class="page-tab" style="left:533px;top:188px">11</span>

    <span class="label" style="left:292px;top:75px">SITE DESIGNS: LUMORA LED</span>
    <div class="body-copy" style="left:292px;top:94px;width:76px">
      <p><span class="drop-cap drop-cap--grey">E</span>Lumora Led are the creators of some of the worlds largest outdoor and indoor Led screens.</p>
    </div>
    <div class="body-copy" style="left:373px;top:94px;width:78px">
      <p>Lumora Led where looking to refresh and modernise their logo. They received over 60 different logo designs from 30 different Designers.</p>
    </div>
    <span class="label" style="left:292px;top:155px">LUMORA WINNER CHOICE</span>
    <div class="logo-panel logo-panel--large">LUMORA LED</div>
    <div class="logo-panel logo-panel--small" style="top:97px">Lumora LED</div>
    <div class="logo-panel logo-panel--small" style="top:163px">Lumora LED</div>
    <div class="logo-panel logo-panel--small" style="top:230px">Lumora LED</div>
    <div class="logo-panel logo-panel--small" style="top:296px">Lumora LED</div>
    <p class="caption" style="left:292px;top:348px">A selection of the 60 different designs that Lumora Led received</p>
    <div class="rule" style="left:292px;top:355px;width:236px"></div>
  </section>
  <span class="page-number" style="left:556px;top:851px">10</span>

  <!-- Spread 11: back cover pocket -->
  <section class="spread spread--pocket" aria-label="Spread 11">
    <div class="rule rule--slate" style="left:20px;top:24px;width:232px"></div>
    <div class="rule rule--slate" style="left:20px;top:351px;width:232px"></div>
    <div class="fold" style="left:270px"></div>
    <svg class="pocket-panel" width="270" height="375" viewBox="0 0 270 375" aria-hidden="true">
      <rect width="270" height="375" fill="var(--slate)"/>
      <path d="M0 375 L0 300 C40 240 110 215 170 232 C215 245 250 280 270 330 L270 375 Z" fill="#fff"/>
      <rect x="50" y="271" width="103" height="95" fill="none" stroke="#9aa6ac" stroke-width="1" stroke-dasharray="3 3"/>
      <line x1="123" y1="258" x2="163" y2="290" stroke="#8a969c" stroke-width="1"/>
      <line x1="46" y1="320" x2="78" y2="352" stroke="#8a969c" stroke-width="1"/>
    </svg>
  </section>
  <span class="page-number" style="left:1148px;top:849px">11</span>

</main>
</body>
</html>
```